Order Management User Interface

I need a new design for our order management screens. They need to be end user friendly and contain the data in an easy to read format. These are online orders. I have attached 3 images from the development solution. For now I just need a new UI and ideally would like it delivered in html so we can easily adapt. The screen has multiple tabs to display the different types of data we store. Ideally the end user needs to see customer focused information first.
I have uploaded an example of a different order view that i like.
Fashion Retail
Coded - Design and coding required
1 page

```html
<!DOCTYPE html>
<html lang="en">
<head>
<meta charset="utf-8">
<title>Order Details</title>
<link href="https://fonts.googleapis.com/css2?family=Poppins:wght@400;500;600&display=swap" rel="stylesheet">
<style>
:root{
  --brand:#2b5797;
  --brand-dark:#244b85;
  --page:#eaeef1;
  --panel:#ffffff;
  --line:#dfe3e8;
  --ink:#1f2a37;
  --muted:#9aa3ad;
  --head:#dde8f7;
  --stripe:#e9f0fa;
  --subhead:#e3e5e8;
  --link:#3d6aaa;
}
*{box-sizing:border-box;margin:0;padding:0}
html,body{width:1200px;height:675px;overflow:hidden}
body{font-family:"Poppins",sans-serif;background:var(--page);color:var(--ink);position:relative}
.sidebar{position:absolute;left:0;top:0;width:43px;height:675px;background:var(--brand)}
.sidebar .nav-icon{position:absolute;left:11px;width:21px;height:21px;display:flex;align-items:center;justify-content:center}
.topbar{position:absolute;left:43px;top:0;right:0;height:34px;background:var(--brand);color:#fff}
.topbar h1{position:absolute;left:18px;top:3px;font-size:20px;font-weight:600;letter-spacing:.2px}
.view-tabs{position:absolute;left:56px;top:47px;display:flex;height:28px}
.view-tab{display:flex;align-items:center;gap:6px;padding:0 15px;font-size:11.5px;height:28px}
.view-tab.inactive{background:var(--brand);color:#fff}
.view-tab.active{background:#fff;color:var(--brand);margin-left:3px}
.panel{position:absolute;left:56px;top:75px;width:1131px;height:588px;background:var(--panel)}
.field-col{position:absolute;top:25px}
.field{display:flex;align-items:center;height:25px;margin-bottom:9.4px}
.field label{font-size:10.5px;width:91px;flex:none}
.field .input{height:25px;width:157px;border:1px solid var(--line);font-size:10px;color:var(--muted);padding-left:12px;display:flex;align-items:center;position:relative}
.spin{position:absolute;right:0;top:1px;width:14px;height:21px;display:flex;flex-direction:column;gap:1px}
.spin span{flex:1;background:#eef0f2;display:flex;align-items:center;justify-content:center}
.divider{position:absolute;top:25px;width:1px;height:162px;background:var(--line)}
.actions{position:absolute;left:18px;top:213px;display:flex;align-items:center}
.actions .lbl{font-size:10.5px}
.check{width:17px;height:17px;background:var(--brand);border-radius:2px;margin-left:6px;display:flex;align-items:center;justify-content:center}
.btn{height:26px;background:var(--brand);color:#fff;font-size:10.5px;display:flex;align-items:center;gap:5px;padding:0 12px;border-radius:2px;margin-left:6px}
.btn.first{margin-left:31px}
.data-tabs{position:absolute;left:18px;top:270px;display:flex;height:28px}
.data-tab{display:flex;align-items:center;gap:5px;background:var(--brand);color:#fff;font-size:11.5px;padding:0 8px;border-left:1px solid #fff}
.data-tab.active{background:#fff;color:var(--ink);border:none;padding:0 10px}
.items{position:absolute;left:25px;top:304px;width:1080px;border-collapse:collapse;table-layout:fixed;font-size:8.8px}
.items th{background:var(--head);font-weight:400;text-align:left;height:24px;padding-left:7px;border-right:1px solid #fff}
.items td{vertical-align:top;padding:14px 0 0 7px;border-left:1px solid var(--line);border-bottom:1px solid var(--line)}
.items tr.alt td{background:var(--stripe)}
.items td.expand{text-align:center;padding-left:0;padding-top:13px;font-size:12px}
.items tr.r1 td{height:79px}
.items tr.r2 td{height:79px}
.items tr.r3 td{height:77px}
.items td.product{padding:15px 0 0 9px}
.product-grid{border-collapse:collapse;table-layout:fixed;width:405px;background:#fff;font-size:8.8px}
.product-grid th{background:var(--subhead);color:var(--link);height:25px;padding-left:10px;border-right:1px solid #fff;font-size:9px}
.product-grid td{height:26px;padding:0 0 0 11px;vertical-align:middle;border:1px solid var(--line);border-top:none;background:#fff!important}
.desc{display:flex;justify-content:space-between;padding-right:6px}
</style>
</head>
<body>
<aside class="sidebar">
  <div class="nav-icon" style="top:5px"><svg width="14" height="12"><rect y="0" width="14" height="2" fill="#fff"/><rect y="5" width="14" height="2" fill="#fff"/><rect y="10" width="14" height="2" fill="#fff"/></svg></div>
  <div class="nav-icon" style="top:42px"><svg width="13" height="12"><path d="M0 1h2l2 7h7l1-5H3" stroke="#fff" stroke-width="1.5" fill="none"/><circle cx="5" cy="10.5" r="1.2" fill="#fff"/><circle cx="10" cy="10.5" r="1.2" fill="#fff"/></svg></div>
  <div class="nav-icon" style="top:80px"><svg width="15" height="11"><rect x=".5" y=".5" width="14" height="10" fill="none" stroke="#fff"/><path d="M3 2v7M5 2v7M7 2v7M9 2v7M11 2v7" stroke="#fff"/></svg></div>
  <div class="nav-icon" style="top:117px"><svg width="8" height="8"><circle cx="4" cy="4" r="4" fill="#fff"/></svg></div>
  <div class="nav-icon" style="top:155px"><svg width="11" height="14"><path d="M5.5 0a5 5 0 0 1 5 5c0 4-5 9-5 9S.5 9 .5 5a5 5 0 0 1 5-5z" fill="#fff"/><circle cx="5.5" cy="5" r="2" fill="#2b5797"/></svg></div>
  <div class="nav-icon" style="top:192px"><svg width="14" height="12"><circle cx="4" cy="2.5" r="2" fill="#fff"/><circle cx="10" cy="2.5" r="2" fill="#fff"/><rect x="1" y="5.5" width="6" height="6.5" rx="1" fill="#fff"/><rect x="7.5" y="5.5" width="6" height="6.5" rx="1" fill="#fff"/></svg></div>
  <div class="nav-icon" style="top:230px"><svg width="14" height="9"><ellipse cx="7" cy="4.5" rx="7" ry="4.5" fill="#fff"/><circle cx="7" cy="4.5" r="2" fill="#2b5797"/></svg></div>
  <div class="nav-icon" style="top:267px"><svg width="11" height="14"><path d="M3 6V4a2.5 2.5 0 0 1 5 0v2" stroke="#fff" stroke-width="1.6" fill="none"/><rect y="6" width="11" height="8" rx="1" fill="#fff"/></svg></div>
</aside>
<header class="topbar"><h1>Development</h1></header>

<nav class="view-tabs">
  <div class="view-tab inactive">Order Search <svg width="11" height="11"><circle cx="5.5" cy="5.5" r="4.8" fill="none" stroke="#fff"/><path d="M3.7 3.7l3.6 3.6M7.3 3.7l-3.6 3.6" stroke="#fff"/></svg></div>
  <div class="view-tab active">Order Details <svg width="11" height="11"><circle cx="5.5" cy="5.5" r="4.8" fill="none" stroke="#2b5797"/><path d="M3.7 3.7l3.6 3.6M7.3 3.7l-3.6 3.6" stroke="#2b5797"/></svg></div>
</nav>

<main class="panel">
  <div class="field-col" style="left:18px">
    <div class="field"><label>Customer No</label><div class="input">Customer No</div></div>
    <div class="field"><label>Firstname</label><div class="input">Daniel</div></div>
    <div class="field"><label>Surname</label><div class="input">Harper</div></div>
    <div class="field"><label>Customer Email</label><div class="input">info@danielharper.com</div></div>
    <div class="field"><label>Created</label><div class="input">21/01/2022 02:05 PM</div></div>
  </div>
  <div class="divider" style="left:282px"></div>
  <div class="field-col" style="left:301px">
    <div class="field"><label>Order No</label><div class="input">9670363</div></div>
    <div class="field"><label>Brand</label><div class="input">Brand Name</div></div>
    <div class="field"><label>Order Type</label><div class="input">Sale</div></div>
    <div class="field"><label>Status</label><div class="input">New</div></div>
    <div class="field"><label>Instructions</label><div class="input">Instructions</div></div>
  </div>
  <div class="divider" style="left:566px"></div>
  <div class="field-col" style="left:584px">
    <div class="field"><label>Total Retail</label><div class="input">105.00<div class="spin"><span></span><span></span></div></div></div>
    <div class="field"><label>Total Tax</label><div class="input">9.55<div class="spin"><span></span><span></span></div></div></div>
    <div class="field"><label>Shipping Amount</label><div class="input">0<div class="spin"><span></span><span></span></div></div></div>
    <div class="field"><label>Shipping Tax</label><div class="input">0<div class="spin"><span></span><span></span></div></div></div>
    <div class="field"><label>Delivery Discount</label><div class="input">0<div class="spin"><span></span><span></span></div></div></div>
  </div>
  <div class="divider" style="left:848px"></div>
  <div class="field-col" style="left:865px">
    <div class="field"><label>Orig Order No</label><div class="input">Orig Order No</div></div>
    <div class="field"><label>Reference</label><div class="input">M9670363</div></div>
    <div class="field"><label>Order Channel</label><div class="input">Standard</div></div>
    <div class="field"><label>Location Code</label><div class="input">1301</div></div>
  </div>

  <div class="actions">
    <span class="lbl">Authority to Leave</span>
    <span class="check"><svg width="10" height="8"><path d="M1 4l3 3 5-6" stroke="#fff" stroke-width="1.6" fill="none"/></svg></span>
    <span class="btn first"><svg width="9" height="9"><rect width="9" height="9" rx="1" fill="#fff"/><rect x="2" y="1" width="5" height="2.5" fill="#2b5797"/></svg>Save</span>
    <span class="btn"><svg width="10" height="10"><path d="M8.5 3.5A4 4 0 1 0 9 6" stroke="#fff" stroke-width="1.6" fill="none"/><path d="M9.5 0v4h-4z" fill="#fff"/></svg>Refresh</span>
  </div>

  <div class="data-tabs">
    <div class="data-tab active"><svg width="11" height="11"><rect x=".5" y=".5" width="10" height="10" rx="2" fill="none" stroke="#1f2a37"/><path d="M5.5 .5v10M.5 5.5h10" stroke="#1f2a37"/></svg>Items</div>
    <div class="data-tab"><svg width="10" height="11"><circle cx="5" cy="3" r="2.5" fill="none" stroke="#fff"/><path d="M.5 10.5a4.5 4.5 0 0 1 9 0z" fill="none" stroke="#fff"/></svg>Customer(s)</div>
    <div class="data-tab"><svg width="11" height="11"><circle cx="5.5" cy="5.5" r="5" fill="none" stroke="#fff"/><circle cx="5.5" cy="5" r="1.8" fill="none" stroke="#fff"/></svg>Addresses</div>
    <div class="data-tab"><svg width="11" height="11"><circle cx="5.5" cy="5.5" r="5" fill="none" stroke="#fff"/><text x="3.6" y="8.2" font-size="7" fill="#fff" font-family="Poppins,sans-serif">$</text></svg>Payments</div>
    <div class="data-tab"><svg width="13" height="11"><path d="M.5 4h12v6.5H.5z" fill="none" stroke="#fff"/><path d="M3 4l4-3.5 3 3.5" fill="none" stroke="#fff"/></svg>Vouchers</div>
    <div class="data-tab"><svg width="11" height="11"><rect x=".5" y="1.5" width="10" height="9" fill="none" stroke="#fff"/><path d="M.5 4h10M3 0v3M8 0v3" stroke="#fff"/></svg>Event Queues</div>
    <div class="data-tab"><svg width="11" height="11"><path d="M9.5 4A4.3 4.3 0 0 0 1.3 4M1.5 7a4.3 4.3 0 0 0 8.2 0" fill="none" stroke="#fff"/><path d="M10 1v3.3H6.8M1 10V6.7h3.2" fill="none" stroke="#fff"/></svg>Updates</div>
    <div class="data-tab"><svg width="11" height="11"><circle cx="5.5" cy="5.5" r="5" fill="none" stroke="#fff"/><path d="M3 5.5l2 2 4-4.5" stroke="#fff" fill="none"/></svg>Fulfilments</div>
    <div class="data-tab"><svg width="11" height="11"><path d="M2 3A4.6 4.6 0 1 1 1 6" fill="none" stroke="#fff"/><path d="M5.5 3v3l2 1.3" stroke="#fff" fill="none"/><path d="M.5 1v3h3" stroke="#fff" fill="none"/></svg>Histiry</div>
  </div>

  <table class="items">
    <colgroup>
      <col style="width:22px"><col style="width:55px"><col style="width:422px"><col style="width:70px"><col style="width:59px"><col style="width:65px"><col style="width:57px"><col style="width:61px"><col style="width:43px"><col style="width:94px"><col style="width:83px"><col style="width:49px">
    </colgroup>
    <thead>
      <tr><th></th><th style="padding-left:12px">SKU</th><th>Product</th><th>Is DropShip</th><th>Quantity</th><th>Unit Retail</th><th>Unit Tax</th><th>Discount</th><th>Final...</th><th>Discount Reason</th><th>Coupon Code</th><th>Status</th></tr>
    </thead>
    <tbody>
      <tr class="r1">
        <td class="expand">+</td><td style="padding-left:12px">2230566</td>
        <td class="product">
          <table class="product-grid">
            <colgroup><col style="width:83px"><col style="width:44px"><col style="width:81px"><col style="width:68px"><col style="width:80px"><col style="width:49px"></colgroup>
            <tr><th>Vendor</th><th>Brand</th><th>Product Code</th><th>Description</th><th>Colour (Code)</th><th>Size</th></tr>
            <tr><td>Lorem Ipsum</td><td style="padding-left:6px">New</td><td style="padding-left:6px">2002569</td><td style="padding-left:6px"><div class="desc">PJ SET <svg width="8" height="8"><path d="M.5.5h7v4l-3 3h-4z" fill="none" stroke="#1f2a37"/></svg></div></td><td style="padding-left:8px">900</td><td style="padding-left:7px">12/14</td></tr>
          </table>
        </td>
        <td>False</td><td>1</td><td>35.00</td><td>03.18</td><td>0.00</td><td>35.00</td><td></td><td></td><td></td>
      </tr>
      <tr class="r2 alt">
        <td class="expand">+</td><td style="padding-left:12px">2230566</td>
        <td class="product">
          <table class="product-grid">
            <colgroup><col style="width:83px"><col style="width:44px"><col style="width:81px"><col style="width:68px"><col style="width:80px"><col style="width:49px"></colgroup>
            <tr><th>Vendor</th><th>Brand</th><th>Product Code</th><th>Description</th><th>Colour (Code)</th><th>Size</th></tr>
            <tr><td>Lorem Ipsum</td><td style="padding-left:6px">New</td><td style="padding-left:6px">2002569</td><td style="padding-left:6px"><div class="desc">PJ SET <svg width="8" height="8"><path d="M.5.5h7v4l-3 3h-4z" fill="none" stroke="#1f2a37"/></svg></div></td><td style="padding-left:8px">900</td><td style="padding-left:7px">12/14</td></tr>
          </table>
        </td>
        <td>False</td><td>1</td><td>35.00</td><td>03.18</td><td>0.00</td><td>35.00</td><td></td><td></td><td></td>
      </tr>
      <tr class="r3">
        <td class="expand">+</td><td style="padding-left:12px">2230566</td>
        <td class="product">
          <table class="product-grid">
            <colgroup><col style="width:83px"><col style="width:44px"><col style="width:81px"><col style="width:68px"><col style="width:80px"><col style="width:49px"></colgroup>
            <tr><th>Vendor</th><th>Brand</th><th>Product Code</th><th>Description</th><th>Colour (Code)</th><th>Size</th></tr>
            <tr><td>Lorem Ipsum</td><td style="padding-left:6px">New</td><td style="padding-left:6px">2002569</td><td style="padding-left:6px"><div class="desc">PJ SET <svg width="8" height="8"><path d="M.5.5h7v4l-3 3h-4z" fill="none" stroke="#1f2a37"/></svg></div></td><td style="padding-left:8px">900</td><td style="padding-left:7px">12/14</td></tr>
          </table>
        </td>
        <td>False</td><td>1</td><td>35.00</td><td>03.18</td><td>0.00</td><td>35.00</td><td></td><td></td><td></td>
      </tr>
    </tbody>
  </table>
</main>
</body>
</html>
```